Redesign of Brochure of company services

We need a redesign a brochure. All of the content on the existing brochure correct, but the design we are not pleased with it. I will provide the previous brochure. Quiet Harbor Fields is Angolan company that provides multiple service ranging providing fruits, vegetables, fisheries, and meat to multiple industries in angola. Quiet Harbor Fields seeks to start delivering or providing their service to home owners looking for fresh products. We want a brochure design that covers all of these aspects.

Target Market(s)

Home owners, middle and upper age mothers, middle and upper class

Industry/Entity Type

Retail

Requirements
Must have
• Logo of the company and the content info
Nice to have
• It's up to you

```html
<!DOCTYPE html>
<html lang="pt">
<head>
<meta charset="utf-8">
<title>Quiet Harbor Fields — Brochura</title>
<link rel="stylesheet" href="https://fonts.googleapis.com/css2?family=Open+Sans:wght@300;400;600&family=Libre+Baskerville:wght@700&display=swap">
<style>
  :root {
    --purple: #5B3A6E;
    --purple-dark: #4A2C5C;
    --orange: #F39A36;
    --orange-red: #E5502A;
    --blue: #1D6A96;
    --red-text: #C8432A;
    --green: #5BA434;
    --grey-text: #555555;
    --white: #FFFFFF;
    --dark: #222222;
  }
  * { margin: 0; padding: 0; box-sizing: border-box; }
  html, body { width: 1200px; height: 848px; overflow: hidden; background: var(--white); }
  body { font-family: "Open Sans", sans-serif; color: var(--grey-text); }
  .brochure { position: relative; width: 1200px; height: 848px; background: var(--white); }
  .abs { position: absolute; }

  .top-band { left: 0; top: 0; width: 800px; height: 50px;
    background: linear-gradient(180deg, var(--purple-dark), var(--purple)); }
  .bookmark { top: 0; width: 58px; height: 72px; }
  .band-label { top: 17px; color: var(--white); font-size: 14px; font-weight: 400; }

  .heading { font-family: "Libre Baskerville", serif; font-weight: 700; color: var(--blue);
    font-size: 18px; letter-spacing: -0.3px; }
  .body-copy { font-size: 13.5px; font-weight: 300; line-height: 22px; color: var(--grey-text); }

  .steps { left: 60px; top: 240px; list-style: none; }
  .steps li { display: flex; align-items: center; height: 62.5px; color: var(--red-text);
    font-size: 14.5px; letter-spacing: 2.2px; font-weight: 400; }
  .steps li svg { margin-right: 6px; }
  .steps li { height: auto; margin-bottom: 44px; }

  .care { left: 60px; top: 422px; color: var(--blue); font-size: 14.5px; letter-spacing: 2.2px; line-height: 26px; }

  .photo { border: none; }
  .photo-cattle { left: 60px; top: 495px; width: 184px; height: 183px;
    background: linear-gradient(180deg, #8FB5D6 0%, #C9D9E0 40%, #6E7A3E 62%, #5B4A32 100%); }
  .photo-farmer { left: 438px; top: 107px; width: 184px; height: 183px;
    background: radial-gradient(circle at 50% 40%, #7A5A34 0%, #3E4A22 55%, #27321A 100%); }
  .photo-produce { left: 800px; top: 196px; width: 400px; height: 225px;
    background: linear-gradient(90deg, #C99A63 0%, #D9B07A 35%, #C58C52 65%, #B98250 100%); }

  .producer-box { left: 0; top: 703px; width: 399px; height: 145px; background: var(--orange); }
  .producer-box p { position: absolute; left: 62px; top: 18px; color: var(--white);
    font-size: 16.5px; letter-spacing: 2.6px; line-height: 21.5px; font-weight: 400; }

  .contact-card { left: 421px; top: 457px; width: 358px; height: 184px; border-radius: 14px;
    background: radial-gradient(ellipse at 30% 40%, #F28A2E 0%, #EE6A2A 55%, var(--orange-red) 100%);
    color: var(--white); padding: 20px 0 0 22px; }
  .contact-card .company { font-size: 16.5px; letter-spacing: 2.6px; margin-bottom: 12px; }
  .contact-card .line { font-size: 16.5px; line-height: 26px; }
  .contact-card .gap { margin-top: 10px; }
  .contact-card .email { letter-spacing: 0.9px; }

  .brand-mark { left: 500px; top: 730px; width: 200px; display: flex; flex-direction: column; align-items: center; }
  .brand-mark .square { width: 44px; height: 44px; background: var(--orange-red); margin-bottom: 14px; }
  .brand-mark .name { font-size: 24px; font-weight: 400; color: var(--dark); white-space: nowrap; }

  .cover-top { left: 800px; top: 0; width: 400px; height: 193px; background: var(--orange); }
  .cover-title { left: 800px; top: 56px; width: 400px; text-align: center; color: var(--white);
    font-size: 24px; font-weight: 400; letter-spacing: 4.5px; line-height: 34px; padding-left: 0; }
  .cover-bottom { left: 800px; top: 425px; width: 400px; height: 423px; background: var(--orange); }
  .cover-tagline { left: 800px; top: 475px; width: 392px; text-align: center; color: var(--white);
    font-size: 19px; line-height: 24px; font-weight: 400; }
</style>
</head>
<body>
<main class="brochure">

  <div class="abs top-band"></div>
  <svg class="abs bookmark" style="left:60px" viewBox="0 0 58 72" aria-hidden="true">
    <path d="M1 0 V70 L29 58 L57 70 V0" fill="#fff" stroke="#6B4A80" stroke-width="1.5"/>
  </svg>
  <svg class="abs bookmark" style="left:438px" viewBox="0 0 58 72" aria-hidden="true">
    <path d="M1 0 V70 L29 58 L57 70 V0" fill="#fff" stroke="#6B4A80" stroke-width="1.5"/>
  </svg>
  <span class="abs band-label" style="left:138px">Frescos de Qualidade</span>
  <span class="abs band-label" style="left:522px">Entregamos à sua porta</span>

  <!-- Inside left panel -->
  <h2 class="abs heading" style="left:59px; top:106px">Confie em Qualidade</h2>
  <p class="abs body-copy" style="left:59px; top:140px; width:300px">A qualidade de todos os frescos distribuídos por nós é verificada para que apenas os produtos aprovados chegem até si.</p>

  <ul class="abs steps">
    <li><svg width="17" height="13" viewBox="0 0 17 13" aria-hidden="true"><path d="M1.5 7 L6 11 L15.5 1.5" fill="none" stroke="var(--green)" stroke-width="3"/></svg>1. Encomende por telefone</li>
    <li><svg width="17" height="13" viewBox="0 0 17 13" aria-hidden="true"><path d="M1.5 7 L6 11 L15.5 1.5" fill="none" stroke="var(--green)" stroke-width="3"/></svg>2. Pague no banco</li>
    <li><svg width="17" height="13" viewBox="0 0 17 13" aria-hidden="true"><path d="M1.5 7 L6 11 L15.5 1.5" fill="none" stroke="var(--green)" stroke-width="3"/></svg>3. Recebaos seus frescos</li>
  </ul>

  <p class="abs care">Manuseamos com cuidado<br>+244 923 410 582</p>

  <div class="abs photo photo-cattle" role="img" aria-label="Photo of a horned bull standing in a sunny green pasture"></div>

  <div class="abs producer-box">
    <p>Se for produtor e deseja<br>comercializar os seus<br>produtos de forma segura,<br>contacte-nos hoje!</p>
  </div>

  <!-- Inside middle panel -->
  <div class="abs photo photo-farmer" role="img" aria-label="Photo of a farmer carrying a basket of fresh produce on his shoulder among green plants"></div>

  <h2 class="abs heading" style="left:440px; top:322px">Fazemos Descontos</h2>
  <p class="abs body-copy" style="left:442px; top:352px; width:200px; font-weight:400; font-size:14px; line-height:21.5px; letter-spacing:0.6px">Fazemos descontos a clientes com contratos de fornecimento contínuo.</p>

  <address class="abs contact-card" style="font-style:normal">
    <div class="company">Quiet Harbor Fields Corp</div>
    <div class="line">Estamos no Vale Sereno</div>
    <div class="line">Luanda, Angola</div>
    <div class="line gap">+244 923 410 582</div>
    <div class="line email">encomendas@quietharborfields.ao</div>
  </address>

  <div class="abs brand-mark">
    <div class="square"></div>
    <div class="name">Quiet Harbor Fields</div>
  </div>

  <!-- Cover panel -->
  <div class="abs cover-top"></div>
  <h1 class="abs cover-title" style="font-weight:400">Hortaliças<br>Frutas Carnes<br>Peixes Mariscos</h1>
  <div class="abs photo photo-produce" role="img" aria-label="Photo of fresh vegetables and fruit on a wooden table: carrots, red cabbage, asparagus, grapes, peppers, potatoes and a bowl of apples"></div>
  <div class="abs cover-bottom"></div>
  <p class="abs cover-tagline">Levamos produtos frescos<br>Nacionais à sua porta.</p>

</main>
</body>
</html>
```